Creative, Colorful, Dynamic Infographic for Global Non-Profit

We are a global arts and education non-profit in need of an infographic that illustrates four key skills embedded in our work: Curiosity, Listening, Imagination, Postive Action.
We work primarily with educators, students, and artists who use the power of personal stories to build community and connection and to bridge divides.
Our new brand guidelines, logos, and fonts are here: https://stylekit.example/lanternfold-9
I've attached a mock-up of the graphic and the required text. (Note the attached design was created by a staff person, your final design does not need to be the same. The color scheme and text of the final design should match the brand guidelines above.)
The graphic will be used for both web and print media and should include the purple Lanternfold 9 logo (also attached).
Ideally the final design will delight audiences and spark interest in our work.

```html
<!DOCTYPE html>
<html lang="en">
<head>
<meta charset="utf-8">
<title>Lanternfold 9 — Four Skills Cycle</title>
<link href="https://fonts.googleapis.com/css2?family=Montserrat:wght@400;900&display=swap" rel="stylesheet">
<style>
  :root {
    --curiosity-red: #ee4243;
    --action-green: #2bb673;
    --listening-purple: #5b3380;
    --imagination-yellow: #fbc113;
    --brand-purple: #633893;
    --ink-light: #ffffff;
    --page: #ffffff;
  }
  html, body {
    margin: 0;
    padding: 0;
    width: 1197px;
    height: 1200px;
    overflow: hidden;
    background: var(--page);
  }
  .skills-cycle {
    display: block;
    width: 1197px;
    height: 1200px;
  }
  .skill-title {
    font-family: "Montserrat", sans-serif;
    font-weight: 900;
    font-size: 40px;
    letter-spacing: 3px;
    fill: var(--ink-light);
  }
  .skill-text, .link-text {
    font-family: "Montserrat", sans-serif;
    font-weight: 400;
    font-size: 21px;
    letter-spacing: 1.6px;
    fill: var(--ink-light);
  }
  .brand-name {
    font-family: "Montserrat", sans-serif;
    font-weight: 400;
    font-size: 30px;
    letter-spacing: 1px;
    fill: var(--ink-light);
  }
  .icon-slot { fill: rgba(255,255,255,0.2); }
  .fill-red { fill: var(--curiosity-red); }
  .fill-green { fill: var(--action-green); }
  .fill-purple { fill: var(--listening-purple); }
  .fill-yellow { fill: var(--imagination-yellow); }
  .fill-brand { fill: var(--brand-purple); }
</style>
</head>
<body>
<svg class="skills-cycle" viewBox="0 0 1500 1500" preserveAspectRatio="none" xmlns="http://www.w3.org/2000/svg">
  <!-- Skill circles -->
  <circle class="fill-red" cx="370" cy="385" r="218"/>
  <circle class="fill-green" cx="1115" cy="385" r="216"/>
  <circle class="fill-purple" cx="375" cy="1120" r="220"/>
  <circle class="fill-yellow" cx="1125" cy="1122" r="218"/>

  <!-- Connecting arrows -->
  <polygon class="fill-green" points="905,318 680,322 680,268 550,355 648,478 652,440 905,445"/>
  <polygon class="fill-red" points="295,590 418,598 418,838 467,835 380,968 258,870 300,862"/>
  <polygon class="fill-purple" points="590,1110 818,1112 818,1060 948,1148 850,1270 848,1225 590,1235"/>
  <polygon class="fill-yellow" points="1098,920 1098,680 1048,680 1135,548 1257,645 1222,650 1222,920"/>

  <!-- Brand mark -->
  <circle class="fill-brand" cx="755" cy="765" r="132"/>
  <text class="brand-name" x="755" y="776" text-anchor="middle">Lanternfold 9</text>

  <!-- Curiosity -->
  <circle class="icon-slot" cx="370" cy="268" r="62" role="img" aria-label="Icon: head outline with question marks"/>
  <text class="skill-title" x="370" y="395" text-anchor="middle">CURIOSITY</text>
  <text class="skill-text" text-anchor="middle">
    <tspan x="373" y="456">Focus on how you can</tspan>
    <tspan x="373" y="483">learn from another’s</tspan>
    <tspan x="373" y="510">knowledge and</tspan>
    <tspan x="373" y="537">experience</tspan>
  </text>

  <!-- Positive action -->
  <circle class="icon-slot" cx="1115" cy="255" r="58" role="img" aria-label="Icon: thumbs-up hand in a circle"/>
  <text class="skill-title" text-anchor="middle">
    <tspan x="1113" y="375">POSITIVE</tspan>
    <tspan x="1113" y="423">ACTION</tspan>
  </text>
  <text class="skill-text" text-anchor="middle">
    <tspan x="1113" y="480">Show your words</tspan>
    <tspan x="1113" y="507">and actions matter</tspan>
  </text>

  <!-- Listening -->
  <circle class="icon-slot" cx="380" cy="1045" r="62" role="img" aria-label="Icon: ear with sound waves"/>
  <text class="skill-title" x="380" y="1170" text-anchor="middle">LISTENING</text>
  <text class="skill-text" text-anchor="middle">
    <tspan x="382" y="1229">Seek to understand</tspan>
    <tspan x="382" y="1256">before speaking</tspan>
  </text>

  <!-- Imagination -->
  <circle class="icon-slot" cx="1128" cy="1020" r="64" role="img" aria-label="Icon: head outline with a cloud and sparkles"/>
  <text class="skill-title" x="1133" y="1152" text-anchor="middle">IMAGINATION</text>
  <text class="skill-text" text-anchor="middle">
    <tspan x="1132" y="1207">Consider possibilities</tspan>
    <tspan x="1132" y="1234">beyond what you know</tspan>
  </text>

  <!-- Arrow captions -->
  <text class="link-text" text-anchor="middle">
    <tspan x="770" y="363">Your positive actions</tspan>
    <tspan x="770" y="388">lead to curiosity about what</tspan>
    <tspan x="770" y="413">else is possible</tspan>
  </text>
  <text class="link-text" transform="translate(365 612) rotate(90)">Your curiosity allows</text>
  <text class="link-text" transform="translate(338 668) rotate(90)">you to listen</text>
  <text class="link-text" text-anchor="middle">
    <tspan x="740" y="1156">Your listening allows</tspan>
    <tspan x="740" y="1182">you to take in new</tspan>
    <tspan x="740" y="1208">information</tspan>
  </text>
  <text class="link-text" transform="translate(1163 635) rotate(90)">Your imagination can</text>
  <text class="link-text" transform="translate(1137 643) rotate(90)">spark positive action</text>
</svg>
</body>
</html>
```